Steel Company / Iron Railing Business Card Template

We are a custom steel fabrication company located in Harlow Falls, PA. In business since 1979, we recently developed a new logo, and we're looking for a business card design to help display the new logo and our business. The name of the company is Kelbrook Forge Co.. The Office Phone number is (610) 555-0143. We fabricate and install custom "wrought iron" railings on our residential side, we also fabricate and erect structural steel (think cranes and steel beams in buildings) on our commercial side. Looking to get a business card template designed. Something modern, but professional. Clear and easy to read. Front should have all business and employee information including phone number(s), email address, business information, etc. back should spotlight logo.

Industry/Entity Type

Construction / Home Improvement

Contact Information for Business Card

Business information is Kelbrook Forge Co., 48 Dunmore Ave Suite 3305, Harlow Falls, PA 19074. Phone number is (610) 555-0143. Website is www.kelbrookforge.example Business card should be for "Tom Pelling" with the job title "Sales & Estimating" but be editable for other employees. Tom's phone number is (610) 555-0178

Colors

Designer to choose colors to be used in the design.

Requirements
Must have
• Modern Feel, Design should be sized for standard business card sizing 3.5" x 2" (88.9mm x 50.8mm)

```html
<!DOCTYPE html>
<html lang="en">
<head>
<meta charset="utf-8">
<title>Kelbrook Forge Co. — Business Card</title>
<link href="https://fonts.googleapis.com/css2?family=Montserrat:wght@400;500;700&family=Roboto+Slab:wght@800&display=swap" rel="stylesheet">
<style>
  :root {
    --stage: #29292b;
    --card-light: #ececec;
    --card-dark: #151516;
    --ink: #141414;
    --ink-soft: #3a3a3a;
    --paper: #f4f4f4;
    --pattern-a: #1c1c1d;
    --pattern-b: #232324;
  }
  * { box-sizing: border-box; margin: 0; padding: 0; }
  html, body {
    width: 1200px; height: 800px; overflow: hidden;
    background: radial-gradient(ellipse at 60% 30%, #38383a 0%, var(--stage) 55%, #1e1e20 100%);
    font-family: "Montserrat", sans-serif;
  }
  .stage {
    width: 1200px; height: 800px;
    display: flex; align-items: center; justify-content: center; gap: 50px;
  }
  .card {
    width: 525px; height: 300px; border-radius: 26px;
    position: relative; overflow: hidden;
    box-shadow: 0 18px 40px rgba(0,0,0,.45);
  }

  /* Back */
  .card-back { background: var(--card-dark); }
  .back-pattern {
    position: absolute; inset: 0;
    background: radial-gradient(circle at 50% 50%, var(--pattern-b) 0%, var(--pattern-a) 70%);
  }
  .back-mark {
    position: absolute; left: 50%; top: 50%; transform: translate(-50%, -50%);
    display: flex; align-items: center; gap: 10px;
    color: var(--paper); font-weight: 700; font-size: 17px; letter-spacing: .04em;
    text-transform: uppercase; white-space: nowrap;
  }
  .back-mark .dot {
    width: 14px; height: 14px; border-radius: 50%; background: var(--paper);
  }

  /* Front */
  .card-front { background: var(--card-light); color: var(--ink); }
  .front-brand {
    position: absolute; left: 34px; top: 0; bottom: 0; width: 215px;
    display: flex; flex-direction: column; align-items: center; justify-content: center; gap: 12px;
  }
  .front-brand .dot {
    width: 22px; height: 22px; border-radius: 50%; background: var(--ink);
  }
  .front-brand .brand-name {
    font-weight: 700; font-size: 24px; line-height: 1.1; text-align: center;
    text-transform: uppercase; letter-spacing: .02em;
  }
  .front-info {
    position: absolute; left: 262px; right: 30px; top: 56px;
  }
  .person-name {
    font-family: "Roboto Slab", serif; font-weight: 800; font-size: 21px;
    letter-spacing: .03em; text-transform: uppercase;
  }
  .person-title { font-size: 12.5px; color: var(--ink-soft); margin-top: 2px; }
  .divider { height: 1.5px; background: var(--ink); margin: 12px -30px 14px 0; }
  .company {
    font-family: "Roboto Slab", serif; font-weight: 800; font-size: 11.5px;
    text-transform: uppercase; letter-spacing: .03em;
  }
  .address { font-size: 12px; line-height: 1.45; color: var(--ink-soft); }
  .contacts { list-style: none; margin-top: 12px; font-size: 12px; color: var(--ink-soft); line-height: 1.55; }
  .contacts li { display: flex; align-items: center; gap: 8px; }
  .contacts svg { width: 11px; height: 11px; fill: var(--ink); flex: none; }
</style>
</head>
<body>
<main class="stage">
  <section class="card card-back" aria-label="Card back">
    <div class="back-pattern" role="img" aria-label="Tone-on-tone repeating company emblem pattern"></div>
    <div class="back-mark"><span class="dot"></span>Kelbrook Forge Co.</div>
  </section>

  <section class="card card-front" aria-label="Card front">
    <div class="front-brand">
      <span class="dot"></span>
      <p class="brand-name">Kelbrook<br>Forge Co.</p>
    </div>
    <div class="front-info">
      <h1 class="person-name">Tom Pelling</h1>
      <p class="person-title">Sales &amp; Estimating</p>
      <div class="divider"></div>
      <p class="company">Kelbrook Forge Co.</p>
      <p class="address">48 Dunmore Ave Suite 3305<br>Harlow Falls, PA 19074</p>
      <ul class="contacts">
        <li><svg viewBox="0 0 24 24"><path d="M6.6 10.8a15.1 15.1 0 0 0 6.6 6.6l2.2-2.2c.3-.3.7-.4 1-.2 1.1.4 2.3.6 3.6.6.6 0 1 .4 1 1V20c0 .6-.4 1-1 1A17 17 0 0 1 3 4c0-.6.4-1 1-1h3.5c.6 0 1 .4 1 1 0 1.3.2 2.5.6 3.6.1.3 0 .7-.2 1z"/></svg>(610) 555-0143</li>
        <li><svg viewBox="0 0 24 24"><path d="M7 1h10a2 2 0 0 1 2 2v18a2 2 0 0 1-2 2H7a2 2 0 0 1-2-2V3a2 2 0 0 1 2-2zm0 3v14h10V4zm5 15.5a1 1 0 1 0 0 2 1 1 0 0 0 0-2z"/></svg>(610) 555-0178</li>
        <li><svg viewBox="0 0 24 24"><path d="M12 2a10 10 0 1 0 0 20 10 10 0 0 0 0-20zm6.9 6h-3a15.6 15.6 0 0 0-1.3-3.9A8 8 0 0 1 18.9 8zM12 4c.8 1.2 1.5 2.5 1.9 4h-3.8c.4-1.5 1.1-2.8 1.9-4zM4.3 14a8 8 0 0 1 0-4h3.4a16.5 16.5 0 0 0 0 4zm.8 2h3a15.6 15.6 0 0 0 1.3 3.9A8 8 0 0 1 5.1 16zm3-8h-3a8 8 0 0 1 4.3-3.9C8.8 5.3 8.4 6.6 8.1 8zM12 20c-.8-1.2-1.5-2.5-1.9-4h3.8c-.4 1.5-1.1 2.8-1.9 4zm2.3-6H9.7a14.7 14.7 0 0 1 0-4h4.6a14.7 14.7 0 0 1 0 4zm.3 5.9c.6-1.2 1-2.5 1.3-3.9h3a8 8 0 0 1-4.3 3.9zm1.7-5.9a16.5 16.5 0 0 0 0-4h3.4a8 8 0 0 1 0 4z"/></svg>www.kelbrookforge.example</li>
      </ul>
    </div>
  </section>
</main>
</body>
</html>
```